Business Card Design needed for logo design project

Our company needs a Business Card Design. Please refer to our original project in the link above.
Dorian Pellworth
Broker

W: Velvetcrestestates.example
P: 555-302-7184
F: 555-741-2096
E: dorianpellworth@mailbox.example
A: North Dallas Office
Updates

Name Spelling update , sorry Dorian Pellworth card is double sided

```html
<!DOCTYPE html>
<html lang="en">
<head>
<meta charset="utf-8">
<title>Velvet Crest Estates – Business Card</title>
<link rel="stylesheet" href="https://fonts.googleapis.com/css2?family=Cinzel:wght@500&family=Montserrat:wght@400;600&display=swap">
<style>
  :root {
    --bronze-dark: #8a5a2b;
    --bronze-mid: #b88a4e;
    --bronze-light: #e6cf8e;
    --leaf-green: #5ce65c;
    --pearl: #e9e9e6;
    --royal-blue: #2f5fd8;
    --royal-blue-light: #4a86ea;
    --ink: #222222;
    --crest-brown: #9c7442;
    --white: #ffffff;
  }
  html, body {
    margin: 0;
    padding: 0;
    width: 1200px;
    height: 720px;
    overflow: hidden;
    background: #ffffff;
  }
  .card {
    position: relative;
    width: 1200px;
    height: 720px;
    overflow: hidden;
    background: linear-gradient(115deg, var(--bronze-dark) 0%, var(--bronze-mid) 38%, var(--bronze-light) 60%, var(--bronze-mid) 80%, var(--bronze-dark) 100%);
  }
  .card-texture {
    position: absolute;
    inset: 0;
    width: 100%;
    height: 100%;
  }
  .brand-panel {
    position: absolute;
    inset: 0;
    width: 1200px;
    height: 720px;
  }
  .name-band {
    position: absolute;
    left: 72px;
    top: 94px;
    width: 560px;
    height: 138px;
    border-radius: 22px 0 0 22px;
    background: linear-gradient(90deg, var(--royal-blue) 0%, var(--royal-blue-light) 100%);
    box-sizing: border-box;
    padding: 18px 0 0 40px;
    font-family: "Montserrat", sans-serif;
    font-weight: 400;
    color: var(--white);
  }
  .name-band .band-line {
    display: block;
    font-size: 36px;
    line-height: 48px;
    letter-spacing: 0.5px;
  }
  .contact-list {
    position: absolute;
    left: 128px;
    top: 276px;
    margin: 0;
    padding: 0;
    list-style: none;
    font-family: "Montserrat", sans-serif;
    font-size: 21px;
    color: var(--ink);
  }
  .contact-list li {
    display: flex;
    align-items: center;
    height: 58px;
    margin-bottom: 14px;
  }
  .contact-icon {
    width: 58px;
    height: 58px;
    margin-right: 12px;
    flex: none;
  }
  .holder {
    position: absolute;
    left: 128px;
    top: 588px;
    font-family: "Montserrat", sans-serif;
    color: var(--ink);
  }
  .holder-name {
    margin: 0;
    font-size: 24px;
    line-height: 32px;
    font-weight: 600;
  }
  .holder-role {
    margin: 2px 0 0;
    font-size: 19px;
    line-height: 26px;
    font-weight: 400;
  }
  .crest-lockup {
    position: absolute;
    left: 760px;
    top: 100px;
    width: 440px;
    text-align: center;
  }
  .crest-disc {
    width: 230px;
    height: 230px;
    margin: 0 auto 44px;
    border-radius: 50%;
    background: var(--crest-brown);
  }
  .crest-name {
    font-family: "Cinzel", serif;
    font-weight: 500;
    color: var(--crest-brown);
    font-size: 42px;
    line-height: 54px;
    letter-spacing: 2px;
    margin: 0;
  }
</style>
</head>
<body>
  <main class="card">
    <svg class="card-texture" viewBox="0 0 1200 720" role="img" aria-label="Fine honeycomb texture over the bronze background">
      <rect width="1200" height="720" fill="#000" opacity="0.04"/>
    </svg>

    <svg class="brand-panel" viewBox="0 0 1200 720" aria-hidden="true">
      <path fill="var(--leaf-green)" d="M715 0 Q575 40 600 150 Q560 240 615 310 Q560 380 590 470 Q600 600 690 720 L1200 720 L1200 0 Z"/>
      <path fill="var(--pearl)" d="M775 0 Q630 60 655 160 Q615 245 668 315 Q620 390 648 475 Q660 610 740 720 L1200 720 L1200 0 Z"/>
    </svg>

    <div class="name-band">
      <span class="band-line">VELVET CREST</span>
      <span class="band-line">ESTATES</span>
    </div>

    <ul class="contact-list">
      <li>
        <svg class="contact-icon" viewBox="0 0 60 60" aria-hidden="true">
          <circle cx="30" cy="30" r="27" fill="none" stroke="var(--ink)" stroke-width="2.5"/>
          <rect x="22" y="14" width="16" height="32" rx="2" fill="none" stroke="var(--ink)" stroke-width="2.5"/>
          <rect x="25" y="18" width="10" height="9" fill="var(--ink)"/>
          <line x1="25" y1="33" x2="35" y2="33" stroke="var(--ink)" stroke-width="2"/>
          <line x1="25" y1="38" x2="35" y2="38" stroke="var(--ink)" stroke-width="2"/>
        </svg>
        <span>+ 555-302-7184</span>
      </li>
      <li>
        <svg class="contact-icon" viewBox="0 0 60 60" aria-hidden="true">
          <circle cx="30" cy="30" r="27" fill="none" stroke="var(--ink)" stroke-width="2.5"/>
          <path d="M13 25 Q30 12 47 25 L43 30 L38 26 L22 26 L17 30 Z" fill="var(--ink)"/>
          <path d="M20 30 L40 30 L44 44 L16 44 Z" fill="var(--ink)"/>
          <circle cx="30" cy="37" r="4" fill="var(--pearl)"/>
        </svg>
        <span>+555-741-2096</span>
      </li>
      <li>
        <svg class="contact-icon" viewBox="0 0 60 60" aria-hidden="true">
          <circle cx="30" cy="30" r="27" fill="none" stroke="var(--ink)" stroke-width="2.5"/>
          <rect x="15" y="20" width="30" height="20" fill="none" stroke="var(--ink)" stroke-width="2.5"/>
          <path d="M15 20 L30 32 L45 20" fill="none" stroke="var(--ink)" stroke-width="2.5"/>
        </svg>
        <span>dorianpellworth@mailbox.example</span>
      </li>
      <li>
        <svg class="contact-icon" viewBox="0 0 60 60" aria-hidden="true">
          <circle cx="30" cy="30" r="27" fill="none" stroke="var(--ink)" stroke-width="2.5"/>
          <circle cx="30" cy="30" r="15" fill="none" stroke="var(--ink)" stroke-width="2"/>
          <ellipse cx="30" cy="30" rx="7" ry="15" fill="none" stroke="var(--ink)" stroke-width="2"/>
          <line x1="15" y1="30" x2="45" y2="30" stroke="var(--ink)" stroke-width="2"/>
          <line x1="18" y1="22" x2="42" y2="22" stroke="var(--ink)" stroke-width="1.6"/>
          <line x1="18" y1="38" x2="42" y2="38" stroke="var(--ink)" stroke-width="1.6"/>
        </svg>
        <span>Velvetcrestestates.example</span>
      </li>
    </ul>

    <div class="holder">
      <p class="holder-name">Dorian Pellworth</p>
      <p class="holder-role">Broker · North Dallas Office</p>
    </div>

    <div class="crest-lockup">
      <div class="crest-disc" aria-hidden="true"></div>
      <p class="crest-name">VELVET CREST<br>ESTATES</p>
    </div>
  </main>
</body>
</html>
```